Consulting Company Business Card

I am looking for a minimalist, classy, professional design on my business card. I would like it to be double-sided. I want to use the font and color scheme of my logo which are attached. Please be creative in the designs that you send me. I want to play off the design of my logo with the inner C that is Green and Blue broken up with the white.
Target Market(s)
Small Businesses
Industry/Entity Type
Consulting
Contact Information for Business Card
Dale M. Whitcombe, CPA CGMA, 555-014-2873, dwhitcombe@vorantaadvisory.example, www.vorantaadvisory.example

```html
<!DOCTYPE html>
<html lang="en">
<head>
<meta charset="utf-8">
<title>Voranta Advisory – Business Card</title>
<link rel="stylesheet" href="https://fonts.googleapis.com/css2?family=Montserrat:wght@700&family=Open+Sans:wght@400;600&display=swap">
<style>
  :root {
    --navy: #262c4e;
    --teal: #267b7b;
    --white: #ffffff;
    --page: #ffffff;
  }
  * { margin: 0; padding: 0; box-sizing: border-box; }
  html, body { width: 1200px; height: 1181px; overflow: hidden; background: var(--page); }
  body { position: relative; font-family: "Open Sans", sans-serif; }

  .card { position: absolute; left: 172px; width: 862px; height: 493px; overflow: hidden; }

  /* Front */
  .card-front { top: 72px; background: var(--navy); }
  .edge-tab { position: absolute; width: 17px; height: 38px; background: var(--white); }
  .edge-tab.left { left: 0; }
  .edge-tab.right { right: 0; }

  .brand { position: absolute; display: flex; flex-direction: column; align-items: center; text-align: center; }
  .brand-mark { border-radius: 50%; background: var(--teal); }
  .brand-name {
    font-family: "Montserrat", sans-serif; font-weight: 700;
    letter-spacing: 0.04em; line-height: 1.05;
  }
  .card-front .brand { left: 0; right: 0; top: 108px; }
  .card-front .brand-mark { width: 96px; height: 96px; margin-bottom: 34px; }
  .card-front .brand-name { color: var(--white); font-size: 42px; }

  /* Back */
  .card-back { top: 606px; background: var(--white); }
  .back-brand-side { position: absolute; left: 0; top: 0; width: 430px; height: 100%; }
  .card-back .brand { left: 0; right: 0; top: 162px; }
  .card-back .brand-mark { width: 78px; height: 78px; margin-bottom: 30px; }
  .card-back .brand-name { color: var(--navy); font-size: 38px; }

  .contact-panel { position: absolute; left: 430px; top: 2px; width: 432px; height: 491px; background: var(--navy); color: var(--white); }

  .name-strip { position: absolute; left: 0; top: 88px; width: 9px; height: 37px; background: var(--white); }
  .person-name {
    position: absolute; left: 19px; top: 88px; height: 37px; padding: 0 4px;
    background: var(--white); color: var(--navy);
    font-weight: 600; font-size: 32px; line-height: 37px; white-space: nowrap;
  }
  .person-title { position: absolute; left: 23px; top: 131px; font-weight: 600; font-size: 25px; line-height: 1.2; }

  .contact-list { list-style: none; }
  .contact-item { position: absolute; left: 0; display: flex; align-items: center; }
  .contact-item::before { content: ""; width: 8px; height: 38px; background: var(--white); margin-right: 9px; }
  .contact-icon {
    width: 39px; height: 39px; border: 1px solid var(--white);
    display: flex; align-items: center; justify-content: center; flex-shrink: 0;
  }
  .contact-icon svg { width: 24px; height: 24px; fill: none; stroke: var(--white); stroke-width: 1.6; stroke-linecap: round; stroke-linejoin: round; }
  .contact-text { margin-left: 12px; font-size: 18.5px; line-height: 1.2; letter-spacing: 0.02em; white-space: nowrap; }
</style>
</head>
<body>

<section class="card card-front" aria-label="Card front">
  <span class="edge-tab left" style="top:151px"></span>
  <span class="edge-tab left" style="top:202px"></span>
  <span class="edge-tab left" style="top:253px"></span>
  <span class="edge-tab left" style="top:303px"></span>
  <span class="edge-tab right" style="top:151px"></span>
  <span class="edge-tab right" style="top:202px"></span>
  <span class="edge-tab right" style="top:253px"></span>
  <span class="edge-tab right" style="top:303px"></span>

  <div class="brand">
    <span class="brand-mark"></span>
    <p class="brand-name">VORANTA<br>ADVISORY</p>
  </div>
</section>

<section class="card card-back" aria-label="Card back">
  <div class="back-brand-side">
    <div class="brand">
      <span class="brand-mark"></span>
      <p class="brand-name">VORANTA<br>ADVISORY</p>
    </div>
  </div>

  <div class="contact-panel">
    <span class="name-strip"></span>
    <h1 class="person-name">Dale M. Whitcombe</h1>
    <p class="person-title">CPA CGMA</p>

    <ul class="contact-list">
      <li class="contact-item" style="top:242px">
        <span class="contact-icon">
          <svg viewBox="0 0 24 24"><path d="M6.5 3.5l3 3.2-1.8 2.2a11 11 0 0 0 7.4 7.4l2.2-1.8 3.2 3-2.2 2.7C10.9 20 4 13.1 3.8 5.7z" fill="#fff" stroke="none"/></svg>
        </span>
        <span class="contact-text">555-014-2873</span>
      </li>
      <li class="contact-item" style="top:293px">
        <span class="contact-icon">
          <svg viewBox="0 0 24 24"><circle cx="12" cy="12" r="9"/><path d="M3 12h18M12 3c-3 3-3 15 0 18M12 3c3 3 3 15 0 18"/></svg>
        </span>
        <span class="contact-text">www.vorantaadvisory.example</span>
      </li>
      <li class="contact-item" style="top:343px">
        <span class="contact-icon">
          <svg viewBox="0 0 24 24"><path d="M21 4L3 10l6 3 2 7 3-5 7-11zM9 13l12-9M11 20l-1-6"/></svg>
        </span>
        <span class="contact-text">dwhitcombe@vorantaadvisory.example</span>
      </li>
      <li class="contact-item" style="top:394px">
        <span class="contact-icon">
          <svg viewBox="0 0 24 24"><path d="M12 21s-6.5-7-6.5-11.5a6.5 6.5 0 0 1 13 0C18.5 14 12 21 12 21z"/><circle cx="12" cy="9.5" r="2.4"/></svg>
        </span>
        <span class="contact-text">418 Harlow Mill Road Brentfield,<br>XY 20417.</span>
      </li>
    </ul>
  </div>
</section>

</body>
</html>
```